PLV Roofing- Bold Web Design Project

We need a website design for a company that constructs and repairs commercial and residential roofing. They need a website design that looks clean, cutting edge, and can keep up with their competitors websites (Norvane Summit, Fulford Roofing Company, TWL Construction). They want to look experienced and "big" enough to handle large commercial projects. They also are striving for a professional and educational feel, and want to really articulate that they work with both residential/HOA and commercial clientele. They want a high conversion rate to their social media platforms and to another area of the site where they can fill out a form, so those areas should be emphasized.

Target Market(s)

Men and Women mainly between 25 and 65, typically in the higher income bracket (200,000+).

Industry/Entity Type

Residential

Requirements
Must have
• Landing page must have two separate but equally prominent buttons, directing the customers to a specific area of the site based on their need: commercial or residential. Clicking ether of these links will lead them to a welcome page for residential customers, or a welcome page for commercial clients.
-So must have 2 pages, a landing page and a welcome page that can be adapted for use as the commercial page and the residential page.
- A photo slider on the landing page
Nice to have
• -Color scheme should generally follow along with the colors used in the logo
-Professional, bold and modern.
Should not have
• -Avoid the "mom and pop" look
-Avoid the color red in the color scheme

```html
<!DOCTYPE html>
<html lang="en">
<head>
<meta charset="utf-8">
<title>PLV Residental</title>
<link href="https://fonts.googleapis.com/css2?family=PT+Sans:wght@400;700&display=swap" rel="stylesheet">
<style>
:root{
  --green:#8dbb1f;
  --green-dark:#6f8a12;
  --green-deep:#62800f;
  --green-text:#7fae1a;
  --ink:#2b2b2b;
  --body:#555;
  --panel:#f4f4f4;
  --line:#e2e2e2;
}
*{box-sizing:border-box;margin:0;padding:0}
html,body{width:1098px;height:1200px;overflow:hidden;background:#fff}
body{position:relative;font-family:Arial,Helvetica,sans-serif;font-size:11px;color:var(--body);line-height:1.3}
.abs{position:absolute}

/* header */
.brand{left:112px;top:54px;font-family:"PT Sans",sans-serif;font-weight:700;font-size:32px;color:var(--ink);display:flex;align-items:center;gap:10px;line-height:1}
.brand .dot{width:18px;height:18px;border-radius:50%;background:var(--green)}
.brand-sub{left:122px;top:106px;font-family:"PT Sans",sans-serif;font-size:7px;color:var(--ink);letter-spacing:.3px}
.contractor{left:613px;top:66px;display:flex;align-items:center;gap:8px;font-family:"PT Sans",sans-serif;font-size:13px;color:var(--ink)}
.head-rule{left:794px;top:48px;width:1px;height:56px;background:var(--line)}
.call{left:824px;top:50px;font-family:"PT Sans",sans-serif;font-size:11.5px;color:var(--ink)}
.call em{font-style:normal;color:var(--green)}
.phone{left:816px;top:66px;display:flex;align-items:center;gap:6px;font-family:"PT Sans",sans-serif;font-weight:700;font-size:22px;color:var(--ink)}

/* navigation */
.nav-band{left:0;top:127px;width:1098px;height:40px;background:linear-gradient(#9dcb2c,#7faf14)}
.nav{left:94px;top:127px;height:40px;display:flex;list-style:none}
.nav li{height:40px;display:flex;align-items:center;justify-content:center;font-family:"PT Sans",sans-serif;font-size:14px;color:#fff;border-right:1px solid rgba(255,255,255,.25)}
.nav li.active{background:linear-gradient(#7aa214,#5f8209)}

/* page title */
.title-bg{left:94px;top:167px;width:906px;height:90px;background:linear-gradient(#f6f6f6,#fff)}
.title-icon{left:110px;top:186px;width:58px;height:48px}
.page-title{left:183px;top:190px;font-family:"PT Sans",sans-serif;font-weight:400;font-size:23px;color:var(--ink)}
.page-sub{left:185px;top:219px;font-size:11.5px;color:var(--ink)}

/* main column */
.main{left:116px;top:262px;width:554px}
.main h2{font-family:"PT Sans",sans-serif;font-weight:400;font-size:17px;color:var(--ink);margin-bottom:2px}
.main p{margin-bottom:14px}
.features{list-style:none;margin:18px 0 22px}
.features li{position:relative;padding-left:24px;margin-bottom:10px}
.features li svg{position:absolute;left:0;top:1px}
.features h3{font-family:"PT Sans",sans-serif;font-size:13px;color:var(--ink);margin-bottom:1px}
.gallery-h{margin-top:30px}
.thumbs{display:grid;grid-template-columns:repeat(6,73px);gap:18px 18.5px;margin-top:14px;margin-left:5px}
.thumb{width:80px;height:72px;padding:4px;background:#fff;box-shadow:0 0 4px rgba(0,0,0,.18)}
.thumb div{width:100%;height:100%}

/* sidebar */
.info{left:705px;top:195px;width:276px;height:182px;background:var(--panel);border:1px solid var(--line);padding:12px 14px}
.info h2{font-family:"PT Sans",sans-serif;font-weight:400;font-size:17px;color:var(--ink);margin-bottom:4px}
.info h3{font-family:"PT Sans",sans-serif;font-size:13px;color:var(--ink);margin:12px 0 4px}
.info a{color:var(--green-text);font-weight:700;text-decoration:none}
.map-frame{left:705px;top:393px;width:276px;height:254px;background:#fff;box-shadow:0 0 5px rgba(0,0,0,.15);padding:8px}
.map{width:100%;height:100%;background:linear-gradient(135deg,#ede8d8,#e6dfc8)}
.testi-h{left:712px;top:674px;font-family:"PT Sans",sans-serif;font-weight:400;font-size:17px;color:var(--ink)}
.quote{left:712px;width:269px;height:80px;background:var(--panel);padding:10px 10px}
.quote::after{content:"";position:absolute;left:16px;bottom:-10px;border-right:10px solid transparent;border-top:10px solid var(--panel)}
.quote cite{display:block;margin-top:4px;font-style:italic;color:var(--green-text)}
.quote cite b{font-weight:700}

/* footer */
.footer{left:0;top:988px;width:1098px;height:183px;background:var(--green-dark)}
.foot-contact{left:139px;top:1054px;font-family:"PT Sans",sans-serif;font-size:11.5px;color:#fff}
.foot-rule{left:513px;top:1025px;width:1px;height:110px;background:rgba(255,255,255,.15)}
.badge{left:546px;top:1038px}
.foot-tag{left:646px;top:1052px;font-family:"PT Sans",sans-serif;font-size:17px;color:#fff;line-height:1.25}
.copy{left:0;top:1171px;width:1098px;height:29px;background:var(--green-deep);border-top:1px solid rgba(255,255,255,.12);color:#fff;text-align:center;font-size:10px;line-height:28px}
</style>
</head>
<body>

<header>
  <div class="abs brand"><span class="dot"></span>PLV Network</div>
  <div class="abs brand-sub">ROOFING &amp; EXTERIOR SERVICES</div>
  <div class="abs contractor">
    <svg width="26" height="20" viewBox="0 0 26 20"><path d="M3 16 Q3 3 14 3 Q24 3 24 14 Z" fill="#f2c21a"/><rect x="1" y="14" width="24" height="4" rx="2" fill="#e0a80f"/></svg>
    Full Service Contractor
  </div>
  <div class="abs head-rule"></div>
  <div class="abs call">Call today for a <em>FREE</em> estimate!</div>
  <div class="abs phone">
    <svg width="20" height="20" viewBox="0 0 20 20"><circle cx="10" cy="10" r="9.5" fill="#8dbb1f"/><path d="M5 7 Q10 3 15 7 L14 9 L12 8 L12 7 Q10 6 8 7 L8 8 L6 9 Z" fill="#fff"/><rect x="6" y="10" width="8" height="5" rx="1" fill="#fff"/></svg>
    (555) 201-4470
  </div>
</header>

<div class="abs nav-band"></div>
<ul class="abs nav">
  <li class="active" style="width:94px">Home</li>
  <li style="width:112px">About Us</li>
  <li style="width:112px">Services</li>
  <li style="width:216px">Insurance &amp; Storm Damage</li>
  <li style="width:120px">Ventilation</li>
  <li style="width:112px">Products</li>
  <li style="width:135px;border-right:0">Contact Us</li>
</ul>

<div class="abs title-bg"></div>
<svg class="abs title-icon" viewBox="0 0 58 48" aria-hidden="true">
  <path d="M2 14 L20 8 L38 14 L56 8 L56 42 L38 48 L20 42 L2 48 Z" fill="#9ccc3a"/>
  <path d="M20 8 L38 14 L38 48 L20 42 Z" fill="#5ea6d9"/>
  <path d="M30 2 a8 8 0 0 1 8 8 c0 6 -8 14 -8 14 c0 0 -8 -8 -8 -14 a8 8 0 0 1 8 -8z" fill="#f08a1c"/>
  <circle cx="30" cy="10" r="3" fill="#fff"/>
</svg>
<h1 class="abs page-title">PLV Residental</h1>
<div class="abs page-sub">Welcome to PLV Commercial Residental</div>

<main class="abs main">
  <h2>PLV Residential Services</h2>
  <p>PLV Roofing was founded on the principles of honesty and integrity. We have many years of building experience – including new construction and home remodel, with a primary focus on roofing and siding.</p>
  <ul class="features">
    <li><svg width="15" height="15" viewBox="0 0 15 15"><circle cx="7.5" cy="7.5" r="7.5" fill="#8dbb1f"/><path d="M4 7.5 L6.5 10 L11 5" stroke="#fff" stroke-width="2" fill="none"/></svg>
      <h3>Lorem Ipsum</h3>Lorem ipsum dolor sit amet, consectetur adipisicing elit, sed do eiusmod tempor incididunt ut labore et dolore magna aliqua.</li>
    <li><svg width="15" height="15" viewBox="0 0 15 15"><circle cx="7.5" cy="7.5" r="7.5" fill="#8dbb1f"/><path d="M4 7.5 L6.5 10 L11 5" stroke="#fff" stroke-width="2" fill="none"/></svg>
      <h3>Dolor sit amet</h3>Sed ut perspiciatis unde omnis iste natus error sit voluptatem accusantium doloremque laudantium, totam rem aperiam, eaque ipsa quae ab illo inventore veritatis et quasi architecto beatae vitae dicta sunt explicabo.</li>
    <li><svg width="15" height="15" viewBox="0 0 15 15"><circle cx="7.5" cy="7.5" r="7.5" fill="#8dbb1f"/><path d="M4 7.5 L6.5 10 L11 5" stroke="#fff" stroke-width="2" fill="none"/></svg>
      <h3>Consectetuer adipiscing</h3>Nemo enim ipsam voluptatem quia voluptas sit aspernatur aut odit aut fugit, sed quia consequuntur magni dolores eos qui ratione voluptatem sequi nesciunt.</li>
    <li><svg width="15" height="15" viewBox="0 0 15 15"><circle cx="7.5" cy="7.5" r="7.5" fill="#8dbb1f"/><path d="M4 7.5 L6.5 10 L11 5" stroke="#fff" stroke-width="2" fill="none"/></svg>
      <h3>Ut wisi enim</h3>Neque porro quisquam est, qui dolorem ipsum quia dolor sit amet, consectetur, adipisci velit, sed quia non numquam eius modi tempora incidunt ut labore et dolore magnam aliquam quaerat voluptatem.</li>
  </ul>
  <p>Lorem ipsum dolor sit amet, consectetuer adipiscing elit, sed diam nonummy nibh euismod tincidunt ut laoreet dolore magna aliquam erat volutpat. Ut wisi enim ad minim veniam, quis nostrud exerci tation ullamcorper suscipit lobortis nisl ut aliquip ex ea commodo consequat.</p>
  <p>Duis autem vel eum iriure dolor in hendrerit in vulputate velit esse molestie consequat, vel illum dolore eu feugiat nulla facilisis at vero eros et accumsan et iusto odio dignissim qui blandit praesent luptatum zzril delenit augue duis dolore te feugait nulla facilisi.</p>

  <h2 class="gallery-h">Gallery</h2>
  <p style="margin-bottom:0">Lorem ipsum dolor sit amet, consectetuer adipiscing elit, sed diam nonummy nibh euismod tincidunt ut laoreet dolore magna aliquam erat volutpat.</p>
  <div class="thumbs">
    <div class="thumb"><div role="img" aria-label="Photo of a renovated house front" style="background:linear-gradient(#8a8f96,#c9ccd0)"></div></div>
    <div class="thumb"><div role="img" aria-label="Photo of a house balcony under blue sky" style="background:linear-gradient(#3f7fd0,#8a6a45)"></div></div>
    <div class="thumb"><div role="img" aria-label="Photo of apartment buildings with trees" style="background:linear-gradient(#cfe0ef,#5b7a48)"></div></div>
    <div class="thumb"><div role="img" aria-label="Photo of a modern building corner" style="background:linear-gradient(#5b8fd6,#3a3f46)"></div></div>
    <div class="thumb"><div role="img" aria-label="Photo of a dark facade with stone" style="background:linear-gradient(#2f3b4d,#6a5440)"></div></div>
    <div class="thumb"><div role="img" aria-label="Photo of a tall modern facade" style="background:linear-gradient(#4b86d1,#4a4a4a)"></div></div>
    <div class="thumb"><div role="img" aria-label="Photo of a two storey house with fence" style="background:linear-gradient(#7fa8d8,#6b5a48)"></div></div>
    <div class="thumb"><div role="img" aria-label="Photo of a house roofline" style="background:linear-gradient(#2f6fc8,#7a6650)"></div></div>
    <div class="thumb"><div role="img" aria-label="Photo of a house with swimming pool" style="background:linear-gradient(#a9c6e6,#3fa0c8)"></div></div>
    <div class="thumb"><div role="img" aria-label="Photo of a house balcony under blue sky" style="background:linear-gradient(#3f7fd0,#8a6a45)"></div></div>
    <div class="thumb"><div role="img" aria-label="Photo of apartment buildings with trees" style="background:linear-gradient(#cfe0ef,#5b7a48)"></div></div>
    <div class="thumb"><div role="img" aria-label="Photo of a modern building corner" style="background:linear-gradient(#a9c3e3,#3a3f46)"></div></div>
  </div>
</main>

<aside>
  <section class="abs info">
    <h2>Basic Information</h2>
    PLV Roofing Riverton, MO<br>
    (555) 201-4471 / Fax (555) 201-4472<br>
    Email <a>plvroofing@example.com</a>
    <h3>Office</h3>
    Oakfield, Riverton<br>Marlow<br>Pine Ridge<br>Ashford Springs
  </section>
  <div class="abs map-frame"><div class="map" role="img" aria-label="Street map of the office location"></div></div>
  <h2 class="abs testi-h">Testimonials</h2>
  <blockquote class="abs quote" style="top:704px">Lorem ipsum dolor sit amet, consectetur adipisicing elit, sed do eiusmod tempor incididunt ut labore et dolore magna aliqua.<cite>Daniel, <b>Westbrook</b></cite></blockquote>
  <blockquote class="abs quote" style="top:805px">Lorem ipsum dolor sit amet, consectetur adipisicing elit, sed do eiusmod tempor incididunt ut labore et dolore magna aliqua.<cite>Daniel, <b>Westbrook</b></cite></blockquote>
</aside>

<footer>
  <div class="abs footer"></div>
  <div class="abs foot-contact">PLV Roofing Riverton, MO (555) 201-4471 / Fax (555) 201-4472<br>Email : <i>plvroofing@example.com</i></div>
  <div class="abs foot-rule"></div>
  <svg class="abs badge" width="82" height="72" viewBox="0 0 82 72" aria-label="Warranty badge"><path d="M2 2 H80 L41 70 Z" fill="#e8e8e8" stroke="#fff" stroke-width="2"/></svg>
  <div class="abs foot-tag">We offer around the clock emergency service<br>for unexpected emergencies!</div>
  <div class="abs copy">Copyright © 2011 PLV Network, All right reserved.</div>
</footer>

</body>
</html>
```